Thoroughbred Racing Partnership needs web design

Crest of Fortune Partners is a management group who buys horses and races them on both the West and East coasts. The premise of the business is for an investment as little as $500, anyone can be a partner and own a percentage of a horse(s). This is a low cost way of getting involved in the exciting sport of Thoroughbred Racing, without shouldering the heavy financial responsibility. Our target market is mostly males 40+ but we want to include all target markets. We are looking for something very clean and professional, we want to give an image of success. Nothing overly "artsy." I have included the logo in which you can incorporate in the site. Also, the logo colors will be the colors of our "silks." The silks are what the jockey wears and will be an important marketing tool for COF. We would like a very prominent picture of a racehorse somewhere on the homepage, we want to make it clear that is a website for Horseracing partnerships.

On the top of the site, it should say "Crest of Fortune" (on the top)
and below that "Thoroughbred Racing Partnerships." (below that)

The main sections, which should be across the top are:

Home
About Us
Ownership
Stable Roster
News
Contact us

Some of these will have drop down menus.

An example of a competitor website that we like is: www.harlowfieldeq.example
An example of a competitor website that we don't like is: www.gallopvane.example
Updates

Project Deadline Extended
Reason: We have a Board of Directors meeting on the 22nd and we will be making a decision on that day. I'm giving an extension so that all designers are able to submit their designs by the 22nd. Thank you!

Target Market(s)

40+ males

Industry/Entity Type

Business

Requirements
Must have
• our logo must be on the site. We would like at least one bold image of a thoroughbred horse in action. The picture is going to tell the story so it needs to be very eye-catching.

Our slogan should also be included on the website, "Experience the thrill of owning a Racehorse."
Should not have
• cartoons, artsy pictures, pictures of Steeplechase horses or "jumpers." This partnership is for racehorses only, there is not jumping involved with the horses.

```html
<!DOCTYPE html>
<html lang="en">
<head>
<meta charset="utf-8">
<title>Crest of Fortune Partners – Thoroughbred Racing Partnerships</title>
<link href="https://fonts.googleapis.com/css2?family=PT+Sans+Narrow:wght@400;700&family=Open+Sans:wght@600;700&family=Roboto:wght@300;400;700&display=swap" rel="stylesheet">
<style>
:root{
  --navy:#0d3a6b;
  --navy-deep:#06335f;
  --accent:#6f9fbf;
  --accent-light:#8bb6d4;
  --dark:#161616;
  --panel:#262626;
  --rule:#444;
  --text-soft:#c9c9c9;
  --white:#fff;
}
*{box-sizing:border-box;margin:0;padding:0}
html,body{width:1034px;height:1200px;overflow:hidden;background:var(--dark)}
body{position:relative;font-family:'Roboto',Arial,sans-serif;color:var(--white)}
.abs{position:absolute}

/* hero */
.hero{left:0;top:0;width:1034px;height:557px;
  background:linear-gradient(180deg,#2f6cc0 0%,#5e93d4 30%,#a9c6e6 58%,#c9ad8a 72%,#a88462 100%)}
.hero-rule{left:0;top:557px;width:1034px;height:4px;background:#3a3a3a}
.brand{left:121px;top:17px;width:158px;height:84px;background:var(--white);
  display:flex;flex-direction:column;align-items:center;justify-content:center;gap:2px}
.brand-name{font-family:'Open Sans',sans-serif;font-weight:700;color:var(--navy);font-size:30px;line-height:1}
.brand-sub{font-family:'Open Sans',sans-serif;font-weight:700;color:var(--navy);font-size:14px;line-height:1}
.tagline{left:673px;top:11px;font-family:'Open Sans',sans-serif;font-weight:600;font-size:12px;line-height:20px;color:#eef3f9;text-shadow:0 1px 2px rgba(0,0,0,.4)}
.nav{left:279px;top:60px;width:633px;height:41px;border-radius:0 4px 4px 0;
  background:linear-gradient(#2c2c2c,#050505);display:flex;justify-content:flex-end}
.nav a{font-family:'Open Sans',sans-serif;font-weight:700;font-size:11px;color:var(--white);text-decoration:none;
  display:flex;align-items:center;padding:0 18px;border-left:1px solid #3a3a3a}
.nav a:first-child{border-left:none}
.nav a.active{background:linear-gradient(#7fb0cc,#5a8eaf);color:#f1f7fb;padding:0 19px}
.slogan{left:638px;top:160px;font-family:'PT Sans Narrow',sans-serif;font-weight:700;font-size:37px;line-height:38px;color:#10345f;letter-spacing:-.3px}
.arrow{top:286px}
.dots{left:831px;top:521px;display:flex;gap:8px}
.dots span{width:14px;height:14px;border-radius:50%;background:#f2f2f2;border:2px solid #ddd}
.dots span.on{background:#3d7cad;border-color:#e8eef3}

/* welcome band */
.welcome{left:0;top:561px;width:1034px;height:229px;background:linear-gradient(90deg,#0e0e0e,#1c1c1c 60%,#111)}
.video{left:122px;top:588px;width:300px;height:182px;border:1px solid #555;background:#c9ced3}
.video-frame{left:0;top:0;width:298px;height:153px;background:linear-gradient(160deg,#dfe3e6,#b5bcc2)}
.video-play{left:128px;top:60px;width:42px;height:30px;border-radius:7px;background:#c4302b}
.video-bar{left:0;top:153px;width:298px;height:27px;background:linear-gradient(#2a2a2a,#111)}
.video-track{left:0;top:0;width:298px;height:5px;background:#555}
.video-prog{left:0;top:0;width:25px;height:5px;background:#c4302b}
.video-time{left:73px;top:10px;font-size:8px;color:#ddd;font-family:Arial,sans-serif}
.welcome-title{left:442px;top:591px;font-family:'PT Sans Narrow',sans-serif;font-size:22px;color:var(--accent-light);display:flex;align-items:baseline;gap:6px}
.welcome-title b{font-family:'Open Sans',sans-serif;font-weight:700;color:var(--white);font-size:22px}
.welcome-rule{left:442px;top:630px;width:465px;border-top:1px dotted #555}
.welcome-lead{left:443px;top:638px;font-size:11px;font-weight:700;color:var(--white)}
.welcome-body{left:443px;top:659px;width:466px;font-size:10.3px;line-height:16px;font-weight:300;color:var(--text-soft);text-align:justify;letter-spacing:.2px}
.more{font-size:10.5px;font-style:italic;color:var(--accent);text-decoration:none}

/* columns */
.columns{left:0;top:790px;width:1034px;height:243px;background:var(--panel);border-top:1px solid #333}
.col-rule{top:804px;height:216px;border-left:1px solid #1a1a1a;box-shadow:1px 0 0 #333}
.col-title{font-family:'PT Sans Narrow',sans-serif;font-weight:700;font-size:20px;color:var(--white);width:240px;padding-bottom:3px;border-bottom:1px solid var(--rule)}
.col-title span{font-weight:400;color:var(--accent-light)}
.about-text{left:122px;top:838px;width:240px;font-size:10.3px;line-height:13.7px;color:var(--text-soft);font-weight:300}
.about-list{left:122px;top:936px;list-style:none;font-size:9.8px;font-weight:700;line-height:16px}
.about-list li::before{content:"»";color:#888;margin-right:8px;font-weight:400}
.about-list li.hl{color:var(--accent-light)}
.news-item{left:397px;width:240px;height:57px;border-bottom:1px solid #353535;display:flex;gap:16px}
.date{width:34px;height:34px;border-radius:3px;background:linear-gradient(#d7d7d7,#9f9f9f);color:#3b3b3b;text-align:center;font-weight:700;flex:none;margin-top:2px}
.date b{display:block;font-size:15px;line-height:17px}
.date i{display:block;font-style:normal;font-size:8px;line-height:9px}
.news-item p{font-size:10.3px;line-height:13.7px;color:var(--text-soft);font-weight:300}
.portrait{left:676px;top:843px;width:65px;height:65px;background:linear-gradient(160deg,#c8ccd0,#6f7e8c)}
.quote{left:757px;top:838px;width:150px;font-size:10.3px;line-height:16px;color:var(--text-soft);font-weight:300}
.q-mark{font-family:Georgia,serif;font-weight:700;color:#ccc;font-size:14px}
.q-name{left:757px;top:915px;font-size:11px;font-weight:700;color:var(--accent-light)}
.q-role{left:757px;top:933px;font-size:11px;font-weight:700;color:var(--white)}

/* footer */
.footer{left:0;top:1033px;width:1034px;height:167px;background:linear-gradient(#0f4a80,var(--navy-deep));border-top:2px solid #3d6f9a}
.foot-title{font-family:'Open Sans',sans-serif;font-weight:700;font-size:12px;color:var(--white);padding-bottom:4px;border-bottom:1px solid #336594}
.foot-div{top:1053px;height:122px;border-left:1px solid #0a2b4c;box-shadow:1px 0 0 #24588a}
.links{font-size:10px;color:#e2ebf3;list-style:none;line-height:25px}
.links li::before{content:"›";font-weight:700;font-size:14px;margin-right:10px}
.foot-text{font-size:9.8px;line-height:14px;color:#e2ebf3}
.email-field{left:368px;top:1127px;width:172px;height:22px;background:var(--white);border:1px solid #bbb;color:#777;font-size:9.5px;padding:5px 7px}
.subscribe{left:473px;top:1158px;width:69px;height:20px;border-radius:3px;background:linear-gradient(#8ab6d0,#5c8fb0);color:var(--white);font-size:9.5px;font-weight:700;text-align:center;line-height:20px}
.contact-row{display:flex;gap:10px;align-items:flex-start;font-size:9.8px;line-height:14px;color:#e2ebf3}
.foot-brand{left:784px;top:1062px;width:110px;text-align:center;font-family:'Open Sans',sans-serif;font-weight:700;color:#c8d4df;line-height:1}
.social{top:1150px;width:27px;height:27px;border-radius:50%;background:linear-gradient(#c7d3dc,#8ea4b5)}
</style>
</head>
<body>

<!-- hero -->
<div class="abs hero" role="img" aria-label="Photograph of a horse and rider in action over a sandy track under a blue cloudy sky"></div>
<div class="abs hero-rule"></div>

<div class="abs brand">
  <span class="brand-name">COF</span>
  <span class="brand-sub">PARTNERS.COM</span>
</div>

<div class="abs tagline">CREST OF FORTUNE<br>THOROUGHBRED RACING PARTNERSHIPS</div>

<nav class="abs nav">
  <a class="active" href="#">HOME</a>
  <a href="#">ABOUT US</a>
  <a href="#">OWNERSHIP</a>
  <a href="#">STABLE ROSTER</a>
  <a href="#">NEWS</a>
  <a href="#">CONTACT US</a>
</nav>

<h1 class="abs slogan">Experience the thrill<br>of owning a Racehorse.</h1>

<svg class="abs arrow" style="left:120px" width="16" height="34" viewBox="0 0 16 34"><polyline points="14,2 2,17 14,32" fill="none" stroke="rgba(255,255,255,.7)" stroke-width="1.5"/></svg>
<svg class="abs arrow" style="left:897px" width="16" height="34" viewBox="0 0 16 34"><polyline points="2,2 14,17 2,32" fill="none" stroke="rgba(255,255,255,.8)" stroke-width="1.5"/></svg>

<div class="abs dots"><span class="on"></span><span></span><span></span><span></span></div>

<!-- welcome -->
<section class="abs welcome"></section>
<div class="abs video">
  <div class="abs video-frame" role="img" aria-label="Video still with the partnership name on a light grey background"></div>
  <div class="abs video-play"><svg width="42" height="30" viewBox="0 0 42 30"><polygon points="16,8 28,15 16,22" fill="#fff"/></svg></div>
  <div class="abs video-bar">
    <div class="abs video-track"></div>
    <div class="abs video-prog"></div>
    <svg class="abs" style="left:18px;top:10px" width="12" height="11"><rect x="1" y="0" width="3" height="11" fill="#ccc"/><rect x="7" y="0" width="3" height="11" fill="#ccc"/></svg>
    <svg class="abs" style="left:48px;top:10px" width="16" height="11"><polygon points="0,4 3,4 7,0 7,11 3,7 0,7" fill="#ccc"/><path d="M10 3 Q13 5.5 10 8" stroke="#ccc" fill="none"/></svg>
    <div class="abs video-time"><b style="color:#fff">0:07</b> / 2:54</div>
    <svg class="abs" style="left:232px;top:9px" width="60" height="13"><circle cx="5" cy="6" r="4.5" fill="#aaa"/><rect x="22" y="3" width="11" height="7" fill="#aaa"/><circle cx="46" cy="6" r="5" fill="none" stroke="#aaa" stroke-width="2.5"/><path d="M49 1v-1M59 1h-3M49 12v-0" stroke="#aaa"/></svg>
  </div>
</div>

<h2 class="abs welcome-title">Welcome to <b>COF</b></h2>
<div class="abs welcome-rule"></div>
<p class="abs welcome-lead">Crest of Fortune Partners is a management group who buys horses and races</p>
<p class="abs welcome-body">Crest of Fortune Partners is a management group who buys horses and races them on both the West and East coasts. The premise of the business is for an investment as little as $500, anyone can be a partner and own a percentage of a horse(s). This is a low cost way of getting involved in the exciting sport of Thoroughbred Racing, without shouldering the heavy financial responsibility.</p>
<a class="abs more" style="left:846px;top:755px" href="#">Read More »</a>

<!-- columns -->
<section class="abs columns"></section>
<div class="abs col-rule" style="left:378px"></div>
<div class="abs col-rule" style="left:653px"></div>

<h3 class="abs col-title" style="left:122px;top:805px"><span>Shortly</span> About Us</h3>
<p class="abs about-text">Duis autem veli eum iriure dolor in hendrerit in vulpu tate velit esse molestie consequat, vel illum dolorel feugiatmul nulla facilisis at vero eros et accumsano et iusto odio dignissim qui blandit praesent luptatuli zrilopil delenit augue duis dolore te feugait nullamol facilisi.</p>
<ul class="abs about-list">
  <li>Lorem ipsum dolor sit amet, consectetuer</li>
  <li class="hl">Duis autem veli eum iriure dolor in hendrerit</li>
  <li>Blandit praesent luptatuli zrilopil delenit</li>
</ul>
<a class="abs more" style="left:291px;top:1005px" href="#">Read More »</a>

<h3 class="abs col-title" style="left:397px;top:805px"><span>Latest</span> News &amp; Events</h3>
<div class="abs news-item" style="top:841px"><div class="date"><b>29</b><i>OCT</i></div><p>Lorem ipsum dolor sit amet, consectetu adipiscing elit, sed diam nonummy nibh consecte nonummy nibh.</p></div>
<div class="abs news-item" style="top:898px"><div class="date"><b>29</b><i>OCT</i></div><p>Lorem ipsum dolor sit amet, consectetu adipiscing elit, sed diam nonummy nibh consecte nonummy nibh.</p></div>
<div class="abs news-item" style="top:955px;border-bottom:none"><div class="date"><b>29</b><i>OCT</i></div><p>Lorem ipsum dolor sit amet, consectetu adipiscing elit, sed diam nonummy nibh consecte nonummy nibh.</p></div>
<a class="abs more" style="left:574px;top:1005px" href="#">Read More »</a>

<h3 class="abs col-title" style="left:672px;top:805px"><span>Client</span> Testimonials</h3>
<div class="abs portrait" role="img" aria-label="Portrait photo of the client giving the testimonial"></div>
<p class="abs quote"><span class="q-mark">“</span> Ut wisi enim ad mini veniam, quis nostrud exerci tationullamo corper suscipit lobortis nislutalil uip commodoconsequat. <span class="q-mark">”</span></p>
<p class="abs q-name">Mr. Lorem ipsum sit amet</p>
<p class="abs q-role">Chief Executive</p>
<a class="abs more" style="left:849px;top:1005px" href="#">Read More »</a>

<!-- footer -->
<footer class="abs footer"></footer>
<div class="abs foot-div" style="left:348px"></div>
<div class="abs foot-div" style="left:565px"></div>
<div class="abs foot-div" style="left:761px"></div>

<h4 class="abs foot-title" style="left:123px;top:1057px;width:204px">QUICK LINKS</h4>
<ul class="abs links" style="left:123px;top:1085px"><li>Home</li><li>About Us</li><li>Ownership</li><li>Stable Roster</li></ul>
<ul class="abs links" style="left:242px;top:1085px"><li>News</li><li>Contact Us</li></ul>

<h4 class="abs foot-title" style="left:370px;top:1057px;width:178px">NEWSLETTER</h4>
<p class="abs foot-text" style="left:368px;top:1090px;width:180px">Subscribe to our newsletter to receive our special offers and more.</p>
<div class="abs email-field">Enter your Email Address here</div>
<div class="abs subscribe">SUBSCRIBE</div>

<h4 class="abs foot-title" style="left:586px;top:1057px;width:154px">CONTACT DETAILS</h4>
<div class="abs contact-row" style="left:585px;top:1090px;width:160px">
  <svg width="10" height="15" viewBox="0 0 10 15" style="flex:none"><path d="M5 0a5 5 0 0 1 5 5c0 4-5 10-5 10S0 9 0 5a5 5 0 0 1 5-5z" fill="#fff"/><circle cx="5" cy="5" r="2" fill="#0d3f73"/></svg>
  <span>Sed diam nonummy euismod tincidunt ut laor</span>
</div>
<div class="abs contact-row" style="left:585px;top:1133px">
  <svg width="12" height="12" viewBox="0 0 12 12" style="flex:none"><path d="M2 0l2.5 3-1.5 1.5c.8 1.8 2.2 3.2 4 4L8.5 7 12 9.5 10 12C4 11 1 8 0 2z" fill="#fff"/></svg>
  <span>(000)123-4567</span>
</div>
<div class="abs contact-row" style="left:585px;top:1164px">
  <svg width="12" height="9" viewBox="0 0 12 9" style="flex:none;margin-top:3px"><rect width="12" height="9" fill="#fff"/><polyline points="0,0 6,5 12,0" fill="none" stroke="#0d3f73"/></svg>
  <span>info@cofpartners.example</span>
</div>

<div class="abs foot-brand"><div style="font-size:30px">COF</div><div style="font-size:12.5px;margin-top:3px">PARTNERS.COM</div></div>
<p class="abs foot-text" style="left:797px;top:1123px">Copyright © 2013 Cof.</p>
<div class="abs social" style="left:780px" aria-label="Social link"></div>
<div class="abs social" style="left:816px" aria-label="Social link"></div>
<div class="abs social" style="left:851px" aria-label="Social link"></div>
<div class="abs social" style="left:887px" aria-label="Social link"></div>

</body>
</html>
```